Need Plexora Ads for Tyre Company

Need some plexora ads graphics for our tyre company Tyre Ferns that only operates in the cayman islands.

Need Ratio Ads: 1000x1000, 1910x1000, 300x600

Important things to have the customer know:
-Email : info@tyreferns.example
-Phone: +1 345 555 0142
-Address: 41 Marlow Lane, George Town, Cayman Islands
-Website: tyreferns.example (Please see our website for the tyres we offer)
- Common Car brands that our Tyres are compatible with: Kelvar, Pratova, Zolt Quira, Bexmont, Tavel, Lorimo, Feravi, Drastelmor
- Our tyres are priced from KYD$55-$60
-We offer free installation on tyres when customers come to our facility to get them changed.
-We sell tyres in bulk and individually.

*You can choose which things to add or omit for the best look, feel free to reword any of the above also to better fit in.
*Please keep in mind that these will have to be viewed in small formats aswell since they are for plexora ads. Please ensure everything is readable when zoomed out.

Target Market(s)

car rental companies & individuals who need to get their tyres replace

Industry/Entity Type

Automotive, Tyre replacement, Car Parts

Colors
EB3D1F
EC4F4E
F09395
F8D3D4
FCEDEE

Requirements
Must have
• Phone, Location, Brands that our tyres are compatible with, Same theme as our logo(Red & Black, White), design adapted to the 3 ratios listed above
Nice to have
• Creative advertising

```html
<!DOCTYPE html>
<html lang="en">
<head>
<meta charset="utf-8">
<title>Tyre Ferns – Ad 300x600</title>
<link rel="stylesheet" href="https://fonts.googleapis.com/css2?family=Roboto:wght@400;500;700&family=Oswald:wght@600;700&display=swap">
<style>
  :root {
    --red: #eb3d1f;
    --red-soft: #ec4f4e;
    --red-deep: #b8210f;
    --pink: #f09395;
    --blush: #f8d3d4;
    --white: #ffffff;
    --black: #0c0c0c;
    --charcoal: #1d1d1d;
    --grey: #cfcfcf;
  }
  * { margin: 0; padding: 0; box-sizing: border-box; }
  html, body { width: 1200px; height: 2400px; overflow: hidden; background: var(--black); }
  .ad {
    position: relative;
    width: 1200px;
    height: 2400px;
    overflow: hidden;
    font-family: "Roboto", Arial, sans-serif;
    color: var(--white);
  }
  .tread-backdrop {
    position: absolute;
    inset: 0;
    background:
      radial-gradient(ellipse at 50% 45%, rgba(70,70,70,.55) 0%, rgba(20,20,20,0) 65%),
      linear-gradient(180deg, #141414 0%, #262626 40%, #1a1a1a 70%, #0d0d0d 100%);
  }
  .brand {
    position: absolute;
    top: 120px;
    left: 0;
    width: 100%;
    display: flex;
    justify-content: center;
    align-items: center;
    gap: 28px;
  }
  .brand-dot {
    width: 64px; height: 64px;
    border-radius: 50%;
    background: var(--red);
  }
  .brand-name {
    font-family: "Oswald", Arial, sans-serif;
    font-weight: 700;
    font-size: 120px;
    line-height: 1;
    color: var(--white);
  }
  .features {
    position: absolute;
    top: 545px;
    left: 60px;
    right: 60px;
    list-style: none;
  }
  .feature {
    display: flex;
    align-items: flex-start;
    gap: 36px;
    margin-bottom: 110px;
  }
  .feature-icon {
    flex: none;
    width: 72px; height: 72px;
    margin-top: 14px;
  }
  .feature-text {
    font-size: 68px;
    line-height: 96px;
    font-weight: 400;
  }
  .accent { color: var(--red-soft); }
  .price {
    position: absolute;
    top: 1250px;
    left: 0;
    width: 100%;
    text-align: center;
    font-family: "Oswald", Arial, sans-serif;
    font-weight: 600;
    font-size: 84px;
    line-height: 112px;
    text-transform: uppercase;
  }
  .compatible-brands {
    position: absolute;
    top: 1590px;
    left: 30px;
    right: 30px;
    display: flex;
    justify-content: space-between;
    align-items: center;
    list-style: none;
  }
  .compatible-brands li {
    font-size: 25px;
    font-weight: 700;
    letter-spacing: .5px;
    color: var(--grey);
    text-transform: uppercase;
  }
  .contact-panel {
    position: absolute;
    left: 0;
    bottom: 0;
    width: 1200px;
    height: 720px;
  }
  .contact-panel svg { position: absolute; inset: 0; }
  .contact-list {
    position: absolute;
    top: 210px;
    left: 0;
    width: 100%;
    list-style: none;
    text-align: center;
    font-size: 52px;
    line-height: 104px;
    font-weight: 500;
  }
</style>
</head>
<body>
<main class="ad">
  <div class="tread-backdrop" role="img" aria-label="Dark stacked tyre treads in the background"></div>

  <header class="brand">
    <span class="brand-dot"></span>
    <span class="brand-name">Tyre Ferns</span>
  </header>

  <ul class="features">
    <li class="feature">
      <svg class="feature-icon" viewBox="0 0 72 72" aria-hidden="true">
        <circle cx="36" cy="36" r="34" fill="var(--red)"/>
        <circle cx="36" cy="36" r="16" fill="none" stroke="var(--charcoal)" stroke-width="6"/>
      </svg>
      <p class="feature-text">We offer <span class="accent">free installation</span> on tyres when customers come to our facility to get them changed</p>
    </li>
    <li class="feature">
      <svg class="feature-icon" viewBox="0 0 72 72" aria-hidden="true">
        <circle cx="36" cy="36" r="34" fill="var(--red)"/>
        <circle cx="36" cy="36" r="16" fill="none" stroke="var(--charcoal)" stroke-width="6"/>
      </svg>
      <p class="feature-text">We sell tyres in <span class="accent">bulk and individually</span></p>
    </li>
  </ul>

  <h2 class="price">Our tyres are priced<br>from <span class="accent">KYD$55-$60</span></h2>

  <ul class="compatible-brands">
    <li>Kelvar</li>
    <li>Pratova</li>
    <li>Quira</li>
    <li>Bexmont</li>
    <li>Tavel</li>
    <li>Lorimo</li>
    <li>Feravi</li>
    <li>Drastelmor</li>
  </ul>

  <footer class="contact-panel">
    <svg viewBox="0 0 1200 720" width="1200" height="720" aria-hidden="true">
      <defs>
        <linearGradient id="panelRed" x1="0" y1="0" x2="0" y2="1">
          <stop offset="0" stop-color="#f04a2c"/>
          <stop offset="1" stop-color="#c92a14"/>
        </linearGradient>
      </defs>
      <path d="M0 120 C 300 20, 900 20, 1200 120 L1200 720 L0 720 Z" fill="var(--red-deep)"/>
      <path d="M0 170 C 300 70, 900 70, 1200 170 L1200 720 L0 720 Z" fill="url(#panelRed)"/>
    </svg>
    <ul class="contact-list">
      <li>Email : info@tyreferns.example</li>
      <li>Phone: +1 345 555 0142</li>
      <li>Website: tyreferns.example</li>
      <li>Address: 41 Marlow Lane, George Town,</li>
      <li>Cayman Islands</li>
    </ul>
  </footer>
</main>
</body>
</html>
```